Vexa Medical Aesthetics - Service Flyer

We are looking to have a friend-fold flyer designed that outlines all of the services offered. I am able to provide pricing on all products and outline of services.

We have had a flyer made in the past and the colours were black and white to go with the logo and keep it simple. We would prefer to keep these colours, but are open to adding in a couple of extra complimentary colours which would match our clinic. I have attached the original flyer that was created as well as our logo.

Target Market(s)

Women aged 25-65

Requirements
Must have
• Our website is www.vexaclinicdemo.com
• 555-014-2278
• Facebook: vexaclinic
• Instagram @vexaclinic
• Services to be included are:
• Some pricing has not been listed, but will update shortly
• Quenlix $8/unit
• Myrelt $10/unit
• Dermal Fillers
• (Cheeks, lips, jawline, chin, temples, under eyes, smile lines, smokers lines)
• 1ml syringe $475
• Mini Lip Plump $250
• Non-Surgical Face Lift $1100
• (Choice of 3 areas, eg. lips, jaw contouring, cheeks)
• Facial Treatments:
• Personalized Facial $85
• Organic Facial -$100
• Deep Cleansing / Acne Facial - $120
• Gel Peel (20% Glycolic/10% Lactic/3.2pH) - $75
• Dermaplaning $120
• Microdermabrasion $120
• Microneedling $250
• Microneedling (package of 3) $600
• Platelet-Rich Plasma (PRP) Facial $400
• Platinum Facial (Dermaplaning + Microneedling) $350
• LED Light Therapy $45
• High Frequency $45
• Skin Consultation (Free)
• Permanent Make-Up:
• Microblading $350
• Microblading Touch-Up $50
• Lashline Enhancement - Top Lashline $300
• Lashline Enhancement - Bottom Lashline $350
• Touch-Up Top/Bottom Lashline $50
• Lip Blush $450
• Lip Blush Touch-up $50
• Tattoo Removal $200 (per session)
• Cosmetic Treatments:
• Classic Eyelash Extensions $99
• Classic Fill $45
• Hybrid Eyelash Extensions $120
• Hybrid Fill $55
• Eyelash Lift & Tint $75
• Teeth Whitening $125
• Organic Teeth Whitening $150
• Medical Aesthetics Treatments:
• Laser Hair Removal $35 and up (per session)
• (Consultation and patch test required for all clients)
• Microneedling for Stretch Marks and Scars - $250 +
• Platelet-Rich Plasma (PRP) Hair Restoration - $500
• Scalp Micropigmentation - $500 and up
• The halvoray / laser hair removal write-up should be replaced with the following:
• We believe in providing only the best for our clients. We specialize in a number of Medical Aesthetics Treatments to address common skin and anti-aging concerns among our clients. All of our treatments are non-invasive, highly effective and affordable. Our services are performed by certified professionals, using clinically proven equipment and products approved and certified through Wellfield Bureau.
• We take pride in the high calibre experience we offer our clients and believe that choosing the appropriate certified professional that can deliver the results you desire, is of primary importance. Vexa employs highly qualified professionals, operating under Dr. Martin Okafor, Board Certified Plastic Surgeon acting as the Medical Director, as well as partners of the Tallowmere Medical team.

```html
<!DOCTYPE html>
<html lang="en">
<head>
<meta charset="utf-8">
<title>Vexa Medical Aesthetics – Service Flyer</title>
<link rel="stylesheet" href="https://fonts.googleapis.com/css2?family=Montserrat:wght@400;500;600;700&display=swap">
<style>
:root{
  --ink:#111111;
  --black:#0b0b0b;
  --white:#ffffff;
  --paper:#fbfbfb;
  --blush:#e4c5ba;
  --blush-deep:#d5856f;
  --blush-head:#edb8a6;
  --sage:#d9e3d5;
  --grey-photo:#ececec;
  --text:#222222;
  --bg:#cfcfcf;
}
*{margin:0;padding:0;box-sizing:border-box}
html,body{width:1200px;height:1200px;overflow:hidden}
body{background:var(--bg);font-family:'Montserrat',sans-serif;color:var(--text);position:relative}
.sheet{position:absolute;left:244px;width:712px;height:554px;background:var(--paper);overflow:hidden;box-shadow:0 2px 8px rgba(0,0,0,.25)}
.sheet--outside{top:30px}
.sheet--inside{top:616px}
.fold{position:absolute;top:0;bottom:0;width:14px;background:linear-gradient(90deg,rgba(0,0,0,0),rgba(0,0,0,.05));pointer-events:none}
.shapes{position:absolute;inset:0;width:712px;height:554px}
.photo{position:absolute}
.abs{position:absolute}

/* logo lockup */
.brand{font-weight:500;color:var(--white);letter-spacing:.06em;line-height:1.05;text-transform:uppercase;display:flex;align-items:center;gap:7px}
.brand__name{font-size:26px}
.brand__sub{font-size:11px}
.brand--dark{color:var(--ink)}

/* outside – intro panel */
.intro{left:25px;top:22px;width:186px}
.intro__head{color:var(--blush-deep);font-weight:500;font-size:8.6px;line-height:11px;margin-bottom:12px}
.intro p{font-size:7.3px;line-height:9.5px;text-align:justify;margin-bottom:10px}

/* outside – contact block */
.contact{left:240px;top:0;width:230px;text-align:center;color:var(--white)}
.contact__label{font-size:6.8px;font-weight:600}
.contact__line{font-size:6.6px;display:flex;justify-content:center;align-items:center;gap:4px}
.contact__line svg{width:9px;height:9px}
.social-dot{width:8px;height:8px;border-radius:50%;background:var(--white);display:inline-block}

/* outside – cover panel */
.cover{left:497px;top:0;width:200px;color:var(--white)}
.cover__head{position:absolute;top:125px;left:0;width:200px;color:var(--blush-head);font-weight:700;font-size:9.6px;line-height:12.5px}
.cover__text{position:absolute;top:176px;left:0;width:200px;font-size:9.6px;line-height:12.5px}
.cover__text b{color:var(--blush-head);font-weight:700}
.cover__url{position:absolute;top:246px;left:0;width:150px;height:17px;border-radius:9px;background:var(--blush);color:var(--ink);font-weight:600;font-size:9.4px;line-height:17px;padding-left:10px;letter-spacing:.02em}

/* inside – price lists */
.menu{position:absolute;width:190px}
.menu__title{display:inline-block;background:var(--black);color:var(--white);font-size:8px;font-weight:500;padding:2px 6px;border-radius:0 7px 7px 0;margin-bottom:5px}
.menu__big{font-size:10.4px;font-weight:700;color:var(--ink);margin-bottom:9px;letter-spacing:.01em}
.menu__note{font-size:8.2px;line-height:10px;margin-bottom:6px}
.row{display:flex;align-items:flex-end;font-size:7.8px;line-height:9.6px;margin-bottom:6.2px}
.row__name{white-space:nowrap}
.row__name--wrap{white-space:normal}
.row__dots{flex:1;border-bottom:1px dotted #666;margin:0 3px 2px}
.row__price{font-weight:700;white-space:nowrap}
.row__extra{font-weight:400;margin-left:3px}
.row--plain{display:block}
.small{font-size:7px}
</style>
</head>
<body>

<!-- OUTSIDE SHEET -->
<section class="sheet sheet--outside" aria-label="Flyer outside">
  <div class="photo" role="img" aria-label="Photo of a clinician performing laser hair removal on a client" style="left:0;top:267px;width:238px;height:287px;background:linear-gradient(160deg,#f1f1f1,#d8d2cd 60%,#bfb7b0)"></div>
  <div class="photo" role="img" aria-label="Soft faded portrait of a woman touching her face" style="left:237px;top:0;width:240px;height:554px;background:linear-gradient(180deg,#f4f4f4,#e6e6e6)"></div>
  <svg class="shapes" viewBox="0 0 712 554" aria-hidden="true">
    <path d="M454,0 L712,0 L712,150 C640,230 520,380 483,554 L236,554 C248,420 300,330 371,259 C430,200 468,120 454,0 Z" fill="var(--black)"/>
    <path d="M712,150 C640,230 520,380 483,554 L712,554 Z" fill="var(--sage)"/>
    <path d="M236,554 C248,420 300,330 371,259 C430,200 468,120 454,0" fill="none" stroke="var(--blush)" stroke-width="5"/>
    <path d="M712,150 C640,230 520,380 483,554" fill="none" stroke="var(--blush)" stroke-width="5"/>
    <circle cx="371" cy="259" r="76" fill="var(--white)" stroke="var(--blush)" stroke-width="5"/>
  </svg>
  <div class="photo" role="img" aria-label="Portrait of a woman's face with gloved hands at her temples" style="left:298px;top:186px;width:146px;height:146px;border-radius:50%;background:radial-gradient(circle,#f1ddd2,#e8e2dd 70%)"></div>
  <div class="photo" role="img" aria-label="Woman with arm raised showing smooth underarm" style="left:492px;top:300px;width:220px;height:254px;background:linear-gradient(200deg,var(--sage),#eedad0 70%);clip-path:polygon(100% 0,100% 100%,0 100%,6% 70%,40% 30%)"></div>
  <div class="fold" style="left:223px"></div>
  <div class="fold" style="left:460px"></div>

  <div class="abs intro">
    <p class="intro__head">The halvoray / laser hair removal write-up should be replaced with the following:</p>
    <p>We believe in providing only the best for our clients. We specialize in a number of Medical Aesthetics Treatments to address common skin and anti-aging concerns among our clients. All of our treatments are non-invasive, highly effective and affordable. Our services are performed by certified professionals, using clinically proven equipment and products approved and certified through Wellfield Bureau.</p>
    <p>We take pride in the high calibre experience we offer our clients and believe that choosing the appropriate certified professional that can deliver the results you desire, is of primary importance. Vexa employs highly qualified professionals, operating under Dr. Martin Okafor, Board Certified Plastic Surgeon acting as the Medical Director, as well as partners of the Tallowmere Medical team.</p>
  </div>

  <div class="abs contact">
    <div class="brand" style="position:absolute;top:382px;left:38px"><span class="brand__name">Vexa</span><span class="brand__sub">Medical<br>Aesthetics</span></div>
    <p class="contact__label" style="position:absolute;top:439px;width:230px">To book an appointment or free consultation:</p>
    <div class="contact__line" style="position:absolute;top:453px;width:230px">
      <svg viewBox="0 0 10 10"><circle cx="5" cy="5" r="4.4" fill="none" stroke="#fff" stroke-width=".9"/><path d="M3.4 3 L4.2 2.8 L4.6 4 L4 4.4 Q4.6 5.6 5.6 6 L6 5.4 L7.2 5.8 L7 6.6 Q4 7 3.4 3Z" fill="#fff"/></svg>
      <span>555-014-2278</span>&nbsp;&nbsp;
      <svg viewBox="0 0 10 10"><circle cx="5" cy="5" r="4.4" fill="none" stroke="#fff" stroke-width=".9"/><rect x="2.8" y="3.5" width="4.4" height="3" fill="none" stroke="#fff" stroke-width=".7"/><path d="M2.8 3.5 L5 5.2 L7.2 3.5" fill="none" stroke="#fff" stroke-width=".7"/></svg>
      <span>info@vexaclinicdemo.com</span>
    </div>
    <p class="contact__label" style="position:absolute;top:485px;width:230px">For more information, visit us at</p>
    <div class="contact__line" style="position:absolute;top:498px;width:230px">
      <svg viewBox="0 0 10 10"><circle cx="5" cy="5" r="4.2" fill="none" stroke="#fff" stroke-width=".9"/><ellipse cx="5" cy="5" rx="1.8" ry="4.2" fill="none" stroke="#fff" stroke-width=".7"/><path d="M0.8 5 H9.2" stroke="#fff" stroke-width=".7"/></svg>
      <span>www.vexaclinicdemo.com</span>
    </div>
    <div class="contact__line" style="position:absolute;top:520px;width:230px">
      <span class="social-dot"></span><span>vexaclinic</span>&nbsp;&nbsp;&nbsp;&nbsp;
      <span class="social-dot"></span><span>@vexaclinic</span>
    </div>
  </div>

  <div class="abs cover">
    <div class="brand" style="position:absolute;top:48px;left:0"><span class="brand__name" style="font-size:30px">Vexa</span><span class="brand__sub" style="font-size:12.5px">Medical<br>Aesthetics</span></div>
    <p class="cover__head">Laser Hair Removal is an afordable, safe and effective way to trest unwanted hair-permantly!</p>
    <p class="cover__text"><b>VEXA</b> uses the Corvana HaloBeam ™ Diode Laser- the Gold Standard in Laser Hair Removal!</p>
    <p class="cover__url">www.vexaclinicdemo.com</p>
  </div>
</section>

<!-- INSIDE SHEET -->
<section class="sheet sheet--inside" aria-label="Flyer inside">
  <div class="photo" role="img" aria-label="Woman in white sitting on the floor" style="left:250px;top:337px;width:217px;height:217px;background:radial-gradient(ellipse at 40% 60%,#eadfd8,#f7f7f7 70%)"></div>
  <svg class="shapes" viewBox="0 0 712 554" aria-hidden="true">
    <path d="M0,0 L212,0 C190,70 120,90 70,120 C35,140 12,165 0,190 Z" fill="var(--black)"/>
    <path d="M212,0 C190,70 120,90 70,120 C35,140 12,165 0,190" fill="none" stroke="var(--blush)" stroke-width="5"/>
    <circle cx="122" cy="101" r="78" fill="var(--white)" stroke="var(--blush)" stroke-width="5"/>
    <path d="M712,340 C640,360 600,420 556,554 L712,554 Z" fill="var(--black)"/>
    <path d="M712,340 C640,360 600,420 556,554" fill="none" stroke="var(--blush)" stroke-width="5"/>
    <circle cx="604" cy="455" r="78" fill="var(--white)" stroke="var(--blush)" stroke-width="5"/>
  </svg>
  <div class="photo" role="img" aria-label="Woman's face in profile with gloved hands at her jaw" style="left:50px;top:29px;width:144px;height:144px;border-radius:50%;background:radial-gradient(circle,#f0dcd2,#e2d8d2 70%)"></div>
  <div class="photo" role="img" aria-label="Woman in a towel receiving a facial mask with a brush" style="left:532px;top:383px;width:144px;height:144px;border-radius:50%;background:radial-gradient(circle,#f4e6de,#e4d6cd 70%)"></div>
  <div class="fold" style="left:223px"></div>
  <div class="fold" style="left:460px"></div>

  <div class="menu" style="left:25px;top:208px;width:188px">
    <p class="menu__big">SERVICES TO BE INCLUDED ARE:</p>
    <p class="menu__note">Some pricing has not been listed, but will update shortly</p>
    <div class="row"><span class="row__name">Quenlix</span><span class="row__dots"></span><span class="row__price">$8/unit</span></div>
    <div class="row"><span class="row__name">Myrelt</span><span class="row__dots"></span><span class="row__price">$10/unit</span></div>
    <div class="row row--plain">Dermal Fillers</div>
    <div class="row row--plain">(Cheeks, lips, jawline, chin, temples, under eyes, smile lines, smokers lines)</div>
    <div class="row"><span class="row__name">1ml syringe</span><span class="row__dots"></span><span class="row__price">$475</span></div>
    <div class="row"><span class="row__name">Mini Lip Plump</span><span class="row__dots"></span><span class="row__price">$250</span></div>
    <div class="row"><span class="row__name">Non-Surgical Face Lift</span><span class="row__dots"></span><span class="row__price">$1100</span></div>
    <div class="row row--plain small">(Choice of 3 areas, eg. lips, jaw contouring, cheeks)</div>
    <div style="height:14px"></div>
    <p class="menu__title">Cosmetic Treatments:</p>
    <div class="row"><span class="row__name">Classic Eyelash Extensions</span><span class="row__dots"></span><span class="row__price">$99</span></div>
    <div class="row"><span class="row__name">Classic Fill</span><span class="row__dots"></span><span class="row__price">$45</span></div>
    <div class="row"><span class="row__name">Hybrid Eyelash Extensions</span><span class="row__dots"></span><span class="row__price">$120</span></div>
    <div class="row"><span class="row__name">Hybrid Fill</span><span class="row__dots"></span><span class="row__price">$55</span></div>
    <div class="row"><span class="row__name">Eyelash Lift &amp; Tint</span><span class="row__dots"></span><span class="row__price">$75</span></div>
    <div class="row"><span class="row__name">Teeth Whitening</span><span class="row__dots"></span><span class="row__price">$125</span></div>
    <div class="row"><span class="row__name">Organic Teeth Whitening</span><span class="row__dots"></span><span class="row__price">$150</span></div>
  </div>

  <div class="menu" style="left:262px;top:25px">
    <p class="menu__title">Facial Treatments:</p>
    <div class="row"><span class="row__name">Personalized Facial</span><span class="row__dots"></span><span class="row__price">$85</span></div>
    <div class="row"><span class="row__name">Organic Facial</span><span class="row__dots"></span><span class="row__price">$100</span></div>
    <div class="row"><span class="row__name">Deep Cleansing / Acne Facial</span><span class="row__dots"></span><span class="row__price">$120</span></div>
    <div class="row"><span class="row__name row__name--wrap">Gel Peel<br>(20% Glycolic/10% Lactic/3.2pH)</span><span class="row__dots"></span><span class="row__price">$75</span></div>
    <div class="row"><span class="row__name">Dermaplaning</span><span class="row__dots"></span><span class="row__price">$120</span></div>
    <div class="row"><span class="row__name">Microdermabrasion</span><span class="row__dots"></span><span class="row__price">$120</span></div>
    <div class="row"><span class="row__name">Microneedling</span><span class="row__dots"></span><span class="row__price">$250</span></div>
    <div class="row"><span class="row__name">Microneedling (package of 3)</span><span class="row__dots"></span><span class="row__price">$600</span></div>
    <div class="row"><span class="row__name">Platelet-Rich Plasma (PRP) Facial</span><span class="row__dots"></span><span class="row__price">$400</span></div>
    <div class="row row--plain">Platinum Facial</div>
    <div class="row"><span class="row__name">(Dermaplaning + Microneedling)</span><span class="row__dots"></span><span class="row__price">$350</span></div>
    <div class="row"><span class="row__name">LED Light Therapy</span><span class="row__dots"></span><span class="row__price">$45</span></div>
    <div class="row"><span class="row__name">High Frequency</span><span class="row__dots"></span><span class="row__price">$45</span></div>
    <div class="row row--plain">Skin Consultation <b>(Free)</b></div>
  </div>

  <div class="brand brand--dark abs" style="left:339px;top:339px"><span class="brand__name" style="font-size:19px">Vexa</span><span class="brand__sub" style="font-size:8px">Medical<br>Aesthetics</span></div>

  <div class="menu" style="left:496px;top:24px">
    <p class="menu__title">Permanent Make-Up:</p>
    <div class="row"><span class="row__name">Microblading</span><span class="row__dots"></span><span class="row__price">$350</span></div>
    <div class="row"><span class="row__name">Microblading Touch-Up</span><span class="row__dots"></span><span class="row__price">$50</span></div>
    <div class="row"><span class="row__name row__name--wrap">Lashline Enhancement -<br>Top Lashline</span><span class="row__dots"></span><span class="row__price">$300</span></div>
    <div class="row"><span class="row__name row__name--wrap">Lashline Enhancement -<br>Bottom Lashline</span><span class="row__dots"></span><span class="row__price">$350</span></div>
    <div class="row"><span class="row__name">Touch-Up Top/Bottom Lashline</span><span class="row__dots"></span><span class="row__price">$50</span></div>
    <div class="row"><span class="row__name">Lip Blush</span><span class="row__dots"></span><span class="row__price">$450</span></div>
    <div class="row"><span class="row__name">Lip Blush Touch-up</span><span class="row__dots"></span><span class="row__price">$50</span></div>
    <div class="row"><span class="row__name">Tattoo Removal</span><span class="row__dots"></span><span class="row__price">$200<span class="row__extra">(per session)</span></span></div>
    <div style="height:14px"></div>
    <p class="menu__title">Medical Aesthetics Treatments:</p>
    <div class="row"><span class="row__name row__name--wrap">Laser Hair Removal<br>and up (per session)</span><span class="row__dots" style="margin-bottom:12px"></span><span class="row__price" style="align-self:flex-start">$35</span></div>
    <div class="row row--plain">(Consultation &amp; patch test required for all clients)</div>
    <div class="row"><span class="row__name row__name--wrap">Microneedling for Stretch Marks<br>and Scars</span><span class="row__dots"></span><span class="row__price">$250 +</span></div>
    <div class="row"><span class="row__name row__name--wrap">Platelet-Rich Plasma (PRP)<br>Hair Restoration</span><span class="row__dots"></span><span class="row__price">$500</span></div>
    <div class="row"><span class="row__name row__name--wrap">Scalp Micropigmentation<br>and up</span><span class="row__dots" style="margin-bottom:12px"></span><span class="row__price" style="align-self:flex-start">$500</span></div>
  </div>
</section>

</body>
</html>
```